Pull Up Banner - Recruitment Company

We would like a design for a pull up banner.

For context: we are a recruitment business. We specialise in helping people in healthcare industry to find jobs in Australia.

I have come up with several ideas and text for the banner. Feel free to use the following as you see appropriate:

- Our logo (see attached)
- 'Healthcare Recruitment Agency'
- Some sort of imagine / cartoon of medical professionals (ie. doctor, nurse, physiotherapist, speech pathologist). A cartoon is more friendly than committing to a photo
- 'Empowering your next career move'
- 'Discover tailored opportunities based on your career preferences'
- Dot points (allied health, nursing, medical imaging)
- Contact info at the bottom including our website (www.quellstaffing.com.au, our Instagram handle @quellstaffing, Mobile: XXXX XXX XXX. The title section for contact information could be 'Get in touch:'

Feel free to submit a couple of designs and we can merge aspects that look good on your designs and find the perfect fit.
Thank you
Updates

Hello,

Thank you for your initial submissions to this project. I appreciate the time you've invested.

After reviewing the first attempt, I'd like to share some feedback and initial observations:

- Professionalism and engagement: Is the overall appearance of the banner professional? It's crucial that we have a high-quality design as this will represent our business.

- Image selection: The image (whether cartoon or real people) appears quite generic. Please consider submitting the banner with a few different photos in the middle for us to choose from. Ensure the image is a good fit and not simply a generic stock photo.

- Contact section: Kindly remove the phone number; we no longer wish to include it on the banner. Instead, please include our website (www.quellstaffing.com.au) and Instagram handle (@quellstaffing).

- Color scheme: White, black, and red/pink are preferred, or alternatively, blue. However, please avoid incorporating too many different colors as it may detract from the professional appearance.

We will be printing the design on a banner and require it to look professional and engaging.

Thank you once again for your submissions. I hope the feedback provided above is helpful.

Warm regards,

Target Market(s)

Allied Health Australia

Font styles to use
Serif

Colors
0054AA
0677BA
7BADD7
CADEEF
E8F1F8
0094D4
00A9DD
6FCCEA
C7EBF8
E9F6FB
EB3D1F
EC4F4E
F09395
F8D3D4
FCEDEE

```html
<!DOCTYPE html>
<html lang="en">
<head>
<meta charset="utf-8">
<title>Quell Staffing – Pull Up Banner</title>
<link rel="stylesheet" href="https://fonts.googleapis.com/css2?family=Montserrat:wght@700;800;900&family=Open+Sans:wght@400;600;700&display=swap">
<style>
  :root {
    --backdrop: #e3e2e4;
    --paper: #ffffff;
    --ink: #111111;
    --brand-blue: #2a2fc6;
    --panel-top: #2530c8;
    --panel-bottom: #1a1f7e;
    --divider-grey: #d9d9de;
    --photo-warm: #c9a57a;
    --photo-light: #f1ede6;
    --photo-teal: #1f9a88;
    --on-blue: #ffffff;
  }
  * { margin: 0; padding: 0; box-sizing: border-box; }
  html, body { width: 1074px; height: 1200px; overflow: hidden; }
  body { background: var(--backdrop); position: relative; font-family: "Open Sans", sans-serif; }

  .banner {
    position: absolute;
    left: 307px; top: 42px;
    width: 460px; height: 1115px;
    background: var(--paper);
    overflow: hidden;
    box-shadow: 0 2px 8px rgba(0,0,0,0.08);
  }
  .banner-shapes { position: absolute; inset: 0; width: 460px; height: 1115px; }

  .brand-name {
    position: absolute; left: 0; right: 0; top: 58px;
    text-align: center;
    font-family: "Montserrat", sans-serif;
    font-weight: 800; font-size: 34px; letter-spacing: 2px;
    color: var(--ink);
    text-transform: uppercase;
  }

  .agency-title {
    position: absolute; left: 0; right: 0; top: 152px;
    text-align: center;
    font-family: "Montserrat", sans-serif;
    font-weight: 900;
    color: var(--brand-blue);
    line-height: 1;
  }
  .agency-title .main { display: block; font-size: 51px; letter-spacing: -0.5px; }
  .agency-title .sub { display: block; font-size: 26px; font-weight: 800; margin-top: 4px; letter-spacing: 0.3px; }

  .panel-copy {
    position: absolute; left: 0; right: 0; top: 590px;
    text-align: center; color: var(--on-blue);
  }
  .tagline {
    font-family: "Montserrat", sans-serif;
    font-weight: 900; font-size: 42px; line-height: 1.03;
    text-transform: uppercase;
  }
  .intro { margin-top: 16px; font-size: 19px; line-height: 1.28; font-weight: 600; }

  .specialties { margin-top: 52px; font-size: 22.5px; font-weight: 600; line-height: 1.25; }
  .specialty-row { list-style: none; display: flex; justify-content: center; gap: 16px; }
  .specialty-row li { display: inline-flex; align-items: center; }
  .specialty-row li::before {
    content: ""; display: inline-block; margin-right: 12px;
    border-left: 8px solid var(--on-blue);
    border-top: 5px solid transparent; border-bottom: 5px solid transparent;
  }

  .contact { margin-top: 56px; }
  .contact-heading {
    display: flex; align-items: center; justify-content: center; gap: 18px;
    font-size: 26px; font-weight: 700;
  }
  .contact-heading::before, .contact-heading::after {
    content: ""; width: 88px; height: 2px; background: var(--on-blue);
  }
  .website { margin-top: 10px; font-size: 23px; font-weight: 400; }
  .website strong { font-weight: 700; }
  .handle {
    margin-top: 4px;
    font-family: "Montserrat", sans-serif;
    font-weight: 800; font-size: 46px; letter-spacing: 0.3px; line-height: 1.1;
  }
</style>
</head>
<body>
  <section class="banner">
    <svg class="banner-shapes" viewBox="0 0 460 1115">
      <defs>
        <linearGradient id="photo-tones" x1="0" y1="0" x2="1" y2="0">
          <stop offset="0" stop-color="var(--photo-warm)"/>
          <stop offset="0.4" stop-color="var(--photo-light)"/>
          <stop offset="0.75" stop-color="var(--photo-teal)"/>
          <stop offset="1" stop-color="var(--photo-light)"/>
        </linearGradient>
        <linearGradient id="panel-fill" x1="0" y1="0" x2="0" y2="1">
          <stop offset="0" stop-color="var(--panel-top)"/>
          <stop offset="1" stop-color="var(--panel-bottom)"/>
        </linearGradient>
      </defs>
      <path d="M0,238 C120,300 300,300 460,218 L460,610 L0,610 Z" fill="var(--divider-grey)"/>
      <path class="photo-area" role="img" aria-label="Photo of a smiling nurse in teal scrubs with a stethoscope helping an elderly woman in a beige cardigan"
            d="M0,246 C120,308 300,308 460,226 L460,610 L0,610 Z" fill="url(#photo-tones)"/>
      <path d="M0,580 C120,535 320,505 460,588 L460,1115 L0,1115 Z" fill="var(--divider-grey)"/>
      <path d="M0,592 C120,547 320,517 460,600 L460,1115 L0,1115 Z" fill="url(#panel-fill)"/>
    </svg>

    <div class="brand-name">Quell Staffing</div>

    <h1 class="agency-title">
      <span class="main">HEALTHCARE</span>
      <span class="sub">RECRUITMENT AGENCY</span>
    </h1>

    <div class="panel-copy">
      <h2 class="tagline">Empowering<br>your next<br>career move</h2>
      <p class="intro">Discover tailored opportunities based<br>on your career preferences</p>

      <div class="specialties">
        <ul class="specialty-row"><li>ALLIED HEALTH</li></ul>
        <ul class="specialty-row"><li>NURSING</li><li>MEDICAL IMAGING</li></ul>
      </div>

      <div class="contact">
        <p class="contact-heading">Get in touch</p>
        <p class="website">www.<strong>quellstaffing</strong>.com.au</p>
        <p class="handle">@quellstaffing</p>
      </div>
    </div>
  </section>
</body>
</html>
```